A Dedicated Thank You to my Dad

Proposed Dimensions: Approx. 20" x 30"

For Father's Day, I wrote a dedication to my Dad that encapsulates my gratitude for everything he does, and everything he is. His birthday is on August 3, but it is more important for me to transform this dedication into a meaningful and memorable gift than to meet any deadline. I would love an image that captures the relationship between a father and his son, accompanied by my words of thanks in some sort of font that is appropriate for the message (calligprahy? not sure about that).

I had actually posted the Thank You on Pixelmarrow as a public post, so anyone with an account can read it: https://www.pixelmarrow.example/photo.php?fbid=40872219360548813&set=a.318760942157.6650129.3908471&type=1&theater

Only the words starting with "Thank you ..." should be on the poster.

Target Market(s)

This is a personal gift for my Dad. He doesn't have the best of eyesight, so having the words in a really small font would not be particularly helpful. :-)

Requirements
Must have
• * Personable
* Warm
* Inviting
* Memorable
* Understated more favored over Loud
Should not have
• * An entire palette of colors
* Wacky colors or fonts

```html
<!DOCTYPE html>
<html lang="en">
<head>
<meta charset="utf-8">
<title>Thank You Dad – Happy Birthday</title>
<link rel="stylesheet" href="https://fonts.googleapis.com/css2?family=Antonio:wght@200;300&family=Amatic+SC:wght@700&display=swap">
<style>
  :root {
    --sky-top: #3f7fc4;
    --sky-mid: #8fb6da;
    --sky-haze: #d9e6ee;
    --sun-glow: #fff6d8;
    --horizon: #c9a877;
    --field: #6e4e25;
    --field-deep: #3e2a12;
    --hand-light: #d9d2c6;
    --hand-mid: #b4aa9a;
    --hand-shade: #8e8678;
    --ink-light: #ffffff;
    --ink-shadow: rgba(30, 20, 10, 0.85);
  }
  * { margin: 0; padding: 0; box-sizing: border-box; }
  html, body {
    width: 826px;
    height: 1200px;
    overflow: hidden;
    background: #ffffff;
  }
  .poster {
    position: relative;
    width: 826px;
    height: 1200px;
    overflow: hidden;
    color: var(--ink-light);
  }
  .poster-backdrop {
    position: absolute;
    inset: 0;
    background:
      radial-gradient(ellipse 520px 180px at 18% 52%, rgba(255, 255, 255, 0.55) 0%, rgba(255, 255, 255, 0) 100%),
      radial-gradient(ellipse 340px 260px at 50% 58%, var(--sun-glow) 0%, rgba(255, 240, 200, 0.55) 40%, rgba(255, 240, 200, 0) 100%),
      linear-gradient(to bottom,
        var(--sky-top) 0%,
        var(--sky-mid) 28%,
        var(--sky-haze) 48%,
        var(--horizon) 62%,
        var(--field) 78%,
        var(--field-deep) 100%);
  }
  .hands-photo {
    position: absolute;
    left: 110px;
    top: 305px;
    width: 620px;
    height: 420px;
    border-radius: 48% 52% 46% 54% / 55% 50% 50% 45%;
    background:
      radial-gradient(ellipse 200px 150px at 55% 38%, var(--hand-light) 0%, rgba(217, 210, 198, 0) 100%),
      radial-gradient(ellipse 300px 200px at 45% 55%, var(--hand-mid) 0%, rgba(180, 170, 154, 0.6) 50%, rgba(142, 134, 120, 0) 100%);
    opacity: 0.9;
  }
  .poster-frame {
    position: absolute;
    left: 22px;
    top: 22px;
    right: 22px;
    bottom: 24px;
    border: 3px solid var(--ink-light);
  }
  .poster-title {
    position: absolute;
    top: 52px;
    left: 0;
    right: 0;
    text-align: center;
    font-family: "Antonio", "Oswald", sans-serif;
    font-weight: 200;
    font-size: 78px;
    line-height: 1;
    letter-spacing: 4px;
  }
  .poster-subtitle {
    position: absolute;
    top: 168px;
    left: 0;
    right: 0;
    text-align: center;
    font-family: "Antonio", "Oswald", sans-serif;
    font-weight: 300;
    font-size: 40px;
    line-height: 1;
    letter-spacing: 2px;
  }
  .dedication {
    position: absolute;
    top: 752px;
    left: 34px;
    right: 34px;
    text-align: center;
    font-family: "Amatic SC", "Patrick Hand SC", cursive;
    font-weight: 700;
    font-size: 22px;
    line-height: 28.5px;
    text-shadow: 0 1px 2px var(--ink-shadow), 0 0 4px var(--ink-shadow);
  }
  .dedication-line { display: block; white-space: nowrap; }
  .closing-rule {
    position: absolute;
    top: 1142px;
    left: 272px;
    width: 280px;
    height: 3px;
    background: var(--ink-light);
  }
</style>
</head>
<body>
  <main class="poster">
    <div class="poster-backdrop" role="img" aria-label="Sunlit sky with rays and clouds above a golden field and distant trees"></div>
    <div class="hands-photo" role="img" aria-label="Photograph of a father's hand holding a child's hand against the bright sky"></div>
    <div class="poster-frame"></div>

    <h1 class="poster-title">–THANK YOU DAD–</h1>
    <h2 class="poster-subtitle">HAPPY BIRTHDAY</h2>

    <p class="dedication">
      <span class="dedication-line">Thank you for embracing the unexpected news that you were about to have twins, for buying enough diapers,</span>
      <span class="dedication-line">for always carrying us, for welcoming more people to stay with us, for sitting through more showings,</span>
      <span class="dedication-line">for doggedly trying to teach me that the beach is not to be feared, for working two jobs,</span>
      <span class="dedication-line">for loading us all up in the station wagon, for, as coach, letting me take a fake rabbit's foot onto the soccer field,</span>
      <span class="dedication-line">for being willing to put a hit out on my guitar teacher, for letting me sing in my room, for making car trips with you,</span>
      <span class="dedication-line">for proudly and patiently taking me to my first nerd conference in junior high,</span>
      <span class="dedication-line">for putting up with the commutes you did, for decades, for my dry sense of humor,</span>
      <span class="dedication-line">for finding a way to send three children to college, for never giving up on trying, for mispronouncing,</span>
      <span class="dedication-line">for teaching me to try to find the good, for showing me that there is peace, for demonstrating the fun,</span>
      <span class="dedication-line">for accepting me for who I am, for doing whatever you can to help whoever you can,</span>
      <span class="dedication-line">for trusting me enough, for insisting, year after year, that time with you means more than any gift I could ever purchase.</span>
    </p>

    <div class="closing-rule"></div>
  </main>
</body>
</html>
```